Bright Path Attorneys Billboard Design for Personal Injury Law Firm

Need a billboard design that we can use for different versions. 1400px X 400px jpeg or png
I have attached the logo and the attorney for the billboard. Attorney Marla Benning
Here is a link to our current website brightpathlegalgroup.example

HEADLINE: HIT BY A TRUCK?
SUBHEAD: NO FEE. BIG FIGHT.
877-GRANTLY

HEADLINE: ACCIDENT?
SUBHEAD: NO FEE, UNLESS WE WIN!
877-GRANTLY

HEADLINE: BIG TRUCK. BIG CASE.
SUBHEAD: YOU PAY $0 UPFRONT
877-GRANTLY

Target Market(s)

People in Car Accident

Industry/Entity Type

Personal Injury Attorneys

```html
<!DOCTYPE html>
<html lang="en">
<head>
<meta charset="utf-8">
<title>Bright Path Attorneys Billboard</title>
<link href="https://fonts.googleapis.com/css2?family=Montserrat:wght@400;600;700;800&display=swap" rel="stylesheet">
<style>
  :root {
    --page-bg: #e6e7e9;
    --navy: #0b0928;
    --band: #14152b;
    --band-phone: #171729;
    --rule: #1f3a26;
    --white: #ffffff;
    --green: #5fd041;
    --photo-warm: #e8932a;
    --photo-red: #8a2a22;
    --photo-dark: #2a1c22;
  }
  html, body {
    margin: 0;
    padding: 0;
    width: 1200px;
    height: 600px;
    overflow: hidden;
    background: var(--page-bg);
    font-family: "Montserrat", sans-serif;
  }
  .billboard {
    position: absolute;
    left: 40px;
    top: 140px;
    width: 1120px;
    height: 320px;
    background: var(--navy);
    overflow: hidden;
  }
  .hero-photo {
    position: absolute;
    left: 0;
    top: 0;
    width: 401px;
    height: 320px;
    background:
      linear-gradient(180deg, rgba(11,9,40,0) 45%, rgba(11,9,40,0.85) 80%, var(--navy) 100%),
      radial-gradient(ellipse at 85% 20%, #ffc14a 0%, var(--photo-warm) 25%, rgba(232,147,42,0) 60%),
      linear-gradient(110deg, #5d5a60 0%, var(--photo-red) 30%, var(--photo-dark) 60%, #6a4020 100%);
  }
  .hero-fade {
    position: absolute;
    left: 401px;
    top: 0;
    width: 32px;
    height: 320px;
    background: var(--navy);
  }
  .grid-rule {
    position: absolute;
    background: var(--rule);
  }
  .rule-vertical { left: 433px; top: 0; width: 1px; height: 320px; }
  .rule-top { left: 433px; top: 31px; width: 687px; height: 1px; }
  .rule-mid { left: 433px; top: 159px; width: 687px; height: 1px; }
  .rule-phone { left: 433px; top: 229px; width: 687px; height: 1px; }
  .rule-bottom { left: 433px; top: 289px; width: 687px; height: 1px; }
  .rule-cell { left: 661px; top: 229px; width: 1px; height: 60px; }
  .rule-cell-end { left: 990px; top: 229px; width: 1px; height: 60px; }
  .band-headline {
    position: absolute;
    left: 434px; top: 32px; width: 686px; height: 127px;
    background: var(--band);
  }
  .band-phone {
    position: absolute;
    left: 434px; top: 160px; width: 686px; height: 69px;
    background: var(--band-phone);
  }
  .headline {
    position: absolute;
    left: 449px;
    top: 34px;
    margin: 0;
    font-size: 75px;
    font-weight: 800;
    letter-spacing: -1px;
    color: var(--white);
    line-height: 1;
  }
  .subhead {
    position: absolute;
    left: 451px;
    top: 114px;
    margin: 0;
    font-size: 39px;
    line-height: 1;
    color: var(--white);
    font-weight: 700;
    white-space: nowrap;
  }
  .subhead .accent {
    color: var(--green);
    font-weight: 400;
  }
  .phone {
    position: absolute;
    left: 450px;
    top: 170px;
    margin: 0;
    font-size: 56px;
    font-weight: 600;
    color: var(--white);
    line-height: 1;
    letter-spacing: 0.5px;
  }
  .brand {
    position: absolute;
    left: 449px;
    top: 229px;
    height: 60px;
    display: flex;
    align-items: center;
    gap: 8px;
  }
  .brand-mark {
    width: 12px;
    height: 12px;
    background: var(--green);
  }
  .brand-name {
    font-size: 15px;
    font-weight: 700;
    color: var(--white);
    white-space: nowrap;
  }
  .website {
    position: absolute;
    left: 662px;
    top: 229px;
    width: 328px;
    height: 60px;
    display: flex;
    align-items: center;
    justify-content: center;
    font-size: 17px;
    font-weight: 400;
    letter-spacing: 0.6px;
    color: var(--white);
  }
</style>
</head>
<body>
  <section class="billboard">
    <div class="hero-photo" role="img" aria-label="Photo of a damaged red car after a crash, with warm bokeh lights in the background"></div>
    <div class="hero-fade"></div>

    <div class="band-headline"></div>
    <div class="band-phone"></div>

    <div class="grid-rule rule-vertical"></div>
    <div class="grid-rule rule-top"></div>
    <div class="grid-rule rule-mid"></div>
    <div class="grid-rule rule-phone"></div>
    <div class="grid-rule rule-bottom"></div>
    <div class="grid-rule rule-cell"></div>
    <div class="grid-rule rule-cell-end"></div>

    <h1 class="headline">ACCIDENT?</h1>
    <p class="subhead"><span class="accent">NO</span> FEE, <span class="accent">UNLESS</span> WE WIN!</p>
    <p class="phone">877-GRANTLY</p>

    <div class="brand">
      <span class="brand-mark"></span>
      <span class="brand-name">Bright Path Attorneys</span>
    </div>
    <div class="website">brightpathlegalgroup.example</div>
  </section>
</body>
</html>
```